依頼詳細
新規アプローチの際に持参及び郵送で、内容が1枚で完結出来る内容でお願いします。
①起 国内の生産年齢人口の高齢化問題や、人口減少の課題
特に九州・中国地方では、一部の地域を除き少子高齢化が顕著である事

②承 現在の製造工場での考えうる課題と対策
一部都市部では、留学生の活用、時給の値上げ等により、人員の確保を行っているが、地方では留学生が居ない、そもそも近隣に人がいないと言う問題があり、同様には対応できない状況

③転 しかし、ミルテアでは、1つのケースとして最寄駅から徒歩35分、バスも1日3~4本の工場で1.日本人の採用が可能 2.時給はそれほど上げていない内容 にも関わらず社員の生活環境を整える事で質の高い採用を実現させている、と言う事例があること

④結 今後3年後、5年後を見越した採用計画・手法の見直しの検討材料の1つに、弊社のサービスの実績と、個別の情報提供・提案を受けてみませんか?

と言う上記のポイントを、危機意識を掘り起こしつつ、且つ分かりやすい内容のチラシの作成をお願いしたいします。
記載項目
株式会社ミルテア 〒813-0047 福岡市東区梢台4-27-8
総合エンジニアリング事業(機械・電気・電子・情報) 労働者派遣事業(派40-385207) 有料職業紹介事業(40-57ユ0263)
TEL:092-748-3157 FAX:092-748-3169
HP http://www.kobara-staffnet.com
サイズ
A4
ページ数
片面
希望イメージ
• +5 0 +5
• シンプル
複雑
• 単色
カラフル
• 暗い
明るい
• 日常
高級
• 遊び心
厳粛
• 未来的
伝統的
• 女性的
男性的
希望する色
青系、水色系、黄・オレンジ系
納品ファイル
• 高解像度JPG (.jpg)
• イラストレーター形式 (.ai)
補足説明
会社のHPにも弊社のイメージカラーや紹介が掲載されていますので、宜しければご参照ください。

```html
<!DOCTYPE html>
<html lang="ja">
<head>
<meta charset="utf-8">
<title>株式会社ミルテア 人材サービスのご案内</title>
<link rel="stylesheet" href="https://fonts.googleapis.com/css2?family=Noto+Sans+JP:wght@400;500;700;900&family=Noto+Serif+JP:wght@700;900&display=swap">
<style>
  :root{
    --ink:#1c1c1c;
    --headline:#5a1414;
    --blue:#1f6fb5;
    --blue-deep:#134a86;
    --sky:#bfe3f5;
    --sky-pale:#e8f5fb;
    --orange:#f0a02a;
    --white:#ffffff;
    --grey:#6b6b6b;
  }
  *{margin:0;padding:0;box-sizing:border-box}
  html,body{width:849px;height:1200px;overflow:hidden;background:var(--white)}
  body{font-family:"Noto Sans JP",sans-serif;color:var(--ink)}
  .flyer{position:relative;width:849px;height:1200px;overflow:hidden}

  .hero{position:absolute;left:0;top:0;width:849px;height:760px;
    background:linear-gradient(100deg,#dfe3e6 0%,#c9ced2 35%,#b9a99a 58%,#e6e7e8 75%,#cdd2d6 100%)}
  .headline{position:absolute;left:14px;top:18px;height:470px;writing-mode:vertical-rl;
    font-family:"Noto Serif JP",serif;font-weight:900;font-size:27px;line-height:1.35;letter-spacing:1px;
    color:var(--headline);text-shadow:0 0 3px #fff,0 0 3px #fff,0 0 6px #fff}
  .points{position:absolute;left:140px;top:20px;list-style:none;font-weight:700;font-size:23px;line-height:1.55;
    text-shadow:0 0 3px #fff,0 0 3px #fff,0 0 6px #fff}
  .points li::before{content:"●";margin-right:4px}

  .services{position:absolute;left:0;top:760px;width:849px;height:355px;background:var(--white)}
  .strengths{position:absolute;left:14px;top:18px;font-size:10.5px;line-height:1.7;color:var(--ink)}
  .diagram{position:absolute;left:0;top:0}
  .node{position:absolute;display:flex;align-items:center;justify-content:center;text-align:center;
    border-radius:50%;font-size:10.5px;font-weight:500;line-height:1.35}
  .need{width:78px;height:78px;background:var(--blue);color:var(--white)}
  .need.alt{background:var(--orange)}
  .offer{width:86px;height:86px;background:var(--sky);color:var(--blue-deep);border:2px solid var(--blue)}
  .propose{position:absolute;left:318px;top:218px;width:52px;height:28px;background:var(--blue);color:#fff;
    font-size:12px;font-weight:700;display:flex;align-items:center;justify-content:center}

  .strategy{position:absolute;left:543px;top:8px;width:292px;height:335px;background:var(--sky-pale);
    border:1px solid var(--sky);padding:12px 14px}
  .strategy h2{font-size:15px;font-weight:700;line-height:1.45;text-align:center;color:var(--blue-deep);
    border:2px solid var(--blue);background:var(--white);padding:7px 4px;margin-bottom:12px}
  .strategy p{font-size:10.5px;line-height:1.7;margin-bottom:10px}

  .footer{position:absolute;left:0;top:1115px;width:849px;height:85px;
    background:linear-gradient(180deg,#ffffff 0%,#e9f3fa 100%);border-top:4px solid var(--blue)}
  .brand{position:absolute;left:16px;top:16px;display:flex;align-items:center;gap:8px}
  .brand-mark{width:16px;height:16px;background:var(--blue)}
  .brand-name{font-size:22px;font-weight:700;color:var(--blue-deep)}
  .company{position:absolute;left:150px;top:20px;font-size:22px;font-weight:700;color:var(--ink)}
  .info{position:absolute;left:370px;top:12px;font-size:8px;line-height:1.55;color:var(--ink)}
  .contact{position:absolute;right:16px;top:8px;text-align:right}
  .tel{font-size:26px;font-weight:700;color:var(--blue)}
  .fax,.hp{font-size:11px;color:var(--grey)}
</style>
</head>
<body>
<main class="flyer">
  <section class="hero" role="img" aria-label="倉庫の棚を背景に白いヘルメットをかぶり腕を組む作業服の女性スタッフの写真">
    <h1 class="headline">生産年齢人口の高齢化問題等、<br>人口減少の課題をミルテアでは解決します!</h1>
    <ul class="points">
      <li>人員の確保</li>
      <li>高い採用</li>
      <li>3年後,5年後を<br>&emsp;見越した採用計画</li>
    </ul>
  </section>

  <section class="services">
    <div class="strengths">
      透明性の高い人材派遣サービス<br>
      的確な人材マッチングと細かなアフターフォロー<br>
      質の高い人材派遣
    </div>

    <svg class="diagram" width="540" height="355" viewBox="0 0 540 355" aria-hidden="true">
      <g stroke="#1f6fb5" stroke-width="2" fill="none">
        <line x1="92" y1="215" x2="130" y2="170"/>
        <line x1="92" y1="240" x2="178" y2="265"/>
        <line x1="210" y1="170" x2="300" y2="232"/>
        <line x1="255" y1="265" x2="300" y2="232"/>
        <line x1="370" y1="232" x2="410" y2="120"/>
        <line x1="370" y1="232" x2="410" y2="232"/>
        <line x1="370" y1="232" x2="410" y2="300"/>
      </g>
      <polygon points="300,226 312,232 300,238" fill="#1f6fb5"/>
    </svg>

    <div class="node need" style="left:14px;top:190px">若手の人材が<br>不足している!</div>
    <div class="node need" style="left:128px;top:120px">20名の人員が<br>欲しい!</div>
    <div class="node need alt" style="left:176px;top:228px">生産効率を<br>改善したい!</div>
    <div class="propose">提案</div>
    <div class="node offer" style="left:410px;top:70px">新卒派遣<br>サービス</div>
    <div class="node offer" style="left:410px;top:186px">FMEプレイング<br>マネージャー<br>派遣サービス</div>
    <div class="node offer" style="left:410px;top:262px;width:110px;height:64px;border-radius:32px">生徒とシニアの<br>人材活用</div>

    <aside class="strategy">
      <h2>新卒から熟練まで、<br>ミルテアらしい「活きる人材戦略」</h2>
      <p>ミルテアの特長は企業ニーズを徹底調査し、新しい職人力を発揮することです。私たちは人材リストから単に候補者を送るのではなく、現場に合う人材を選び抜きます。</p>
      <p>個人のニーズと企業のニーズを丁寧にマッチングし、採用後の定着まで寄り添います。住まいや通勤など生活環境を整えることで、地方の工場でも質の高い採用を実現します。</p>
      <p>3年後、5年後を見据えた採用計画づくりを、ミルテアの「活きる人材戦略」がお手伝いします。</p>
    </aside>
  </section>

  <footer class="footer">
    <div class="brand"><span class="brand-mark"></span><span class="brand-name">ミルテア</span></div>
    <div class="company">株式会社ミルテア</div>
    <div class="info">
      〒813-0047 福岡市東区梢台4-27-8<br>
      総合エンジニアリング事業(機械・電気・電子・情報)<br>
      労働者派遣事業(派40-385207)<br>
      有料職業紹介事業(40-57ユ0263)
    </div>
    <div class="contact">
      <div class="tel">☎:092-748-3157</div>
      <div class="fax">FAX:092-748-3169</div>
      <div class="hp">HP http://www.kobara-staffnet.com</div>
    </div>
  </footer>
</main>
</body>
</html>
```